Business Card for an electrical contractor involved in the resource industry
KLM Partners Australia
Business Card for an electrical contractor involved in the resource industry - Construction
Creative Brief
Simple
Derek Fanshaw
Managing Director
Head Office Suite 2716, 58, Moreland St Carrow Flats, NSW 2039
derek@klmpartnersaustralia.com.au
www.klmpartnersaustralia.com.au
Web Address and logo

```html
<!DOCTYPE html>
<html lang="en">
<head>
<meta charset="utf-8">
<title>Orvane Partners Australia – Business Card</title>
<link href="https://fonts.googleapis.com/css2?family=Open+Sans:wght@400;600;700;800&display=swap" rel="stylesheet">
<style>
  :root {
    --backdrop: #e9e7e5;
    --red: #d3172d;
    --red-deep: #a80d20;
    --white: #ffffff;
    --paper-grey: #e4e4e6;
    --grey-edge: #8e8e92;
    --tab-grey: #58585c;
    --ink-grey: #6c6c70;
  }
  * { margin: 0; padding: 0; box-sizing: border-box; }
  html, body {
    width: 1200px; height: 802px; overflow: hidden;
    background: var(--backdrop);
    font-family: "Open Sans", Arial, sans-serif;
  }
  .stage {
    width: 1200px; height: 802px;
    display: flex; align-items: center; justify-content: center; gap: 40px;
  }
  .card {
    position: relative; width: 540px; height: 309px;
    overflow: hidden; box-shadow: 0 6px 18px rgba(0,0,0,.18);
  }
  .card-shapes { position: absolute; inset: 0; width: 100%; height: 100%; }

  /* front */
  .brand { position: absolute; left: 34px; top: 74px; display: flex; align-items: center; gap: 12px; }
  .brand-dot { width: 50px; height: 50px; border-radius: 50%; background: var(--red); flex: none; }
  .brand-name { color: var(--red); font-weight: 800; font-size: 17px; letter-spacing: .5px; line-height: 1.1; }
  .brand-tagline { color: var(--ink-grey); font-size: 7.5px; letter-spacing: .4px; margin-top: 3px; }
  .web-tab {
    position: absolute; left: 296px; top: 158px;
    color: var(--white); font-size: 11.5px; letter-spacing: .3px;
  }
  .contact { position: absolute; color: var(--white); font-size: 10px; line-height: 1.45; display: flex; gap: 8px; align-items: flex-start; }
  .contact svg { flex: none; margin-top: 2px; }
  .contact-phone { left: 28px; top: 214px; }
  .contact-address { left: 28px; top: 256px; font-size: 9.5px; }
  .contact-email { left: 296px; top: 268px; font-size: 11.5px; align-items: center; }

  /* back */
  .person { position: absolute; right: 30px; top: 30px; text-align: right; color: var(--white); }
  .person-name { font-size: 17px; font-weight: 600; letter-spacing: 1.5px; }
  .person-role { font-size: 11px; opacity: .9; margin-top: 2px; }
</style>
</head>
<body>
<main class="stage">

  <section class="card card-front" aria-label="Business card front">
    <svg class="card-shapes" viewBox="0 0 540 309" aria-hidden="true">
      <defs>
        <linearGradient id="redFront" x1="0" y1="0" x2="1" y2="1">
          <stop offset="0" stop-color="#e12a3d"/>
          <stop offset="1" stop-color="#a80d20"/>
        </linearGradient>
        <linearGradient id="paperFront" x1="0" y1="0" x2="0" y2="1">
          <stop offset="0" stop-color="#ffffff"/>
          <stop offset="1" stop-color="#e4e4e6"/>
        </linearGradient>
      </defs>
      <rect width="540" height="309" fill="url(#redFront)"/>
      <path class="band-edge" d="M0,40 H540 V146 H300 Q276,146 266,164 L254,186 Q244,202 222,202 H0 Z" fill="var(--grey-edge)"/>
      <path class="band" d="M0,44 H540 V140 H296 Q272,140 262,158 L250,180 Q241,196 220,196 H0 Z" fill="url(#paperFront)"/>
      <path class="web-tab-shape" d="M300,146 H540 V190 H300 Q278,190 278,168 Q278,146 300,146 Z" fill="var(--tab-grey)"/>
    </svg>

    <div class="brand">
      <span class="brand-dot"></span>
      <div>
        <div class="brand-name">ORVANE PARTNERS AUSTRALIA</div>
        <div class="brand-tagline">Electrical contractor resource industry</div>
      </div>
    </div>

    <div class="web-tab">www.orvanepartners.com.au</div>

    <div class="contact contact-phone">
      <svg width="12" height="12" viewBox="0 0 24 24"><path fill="#fff" d="M6.6 10.8a15.1 15.1 0 0 0 6.6 6.6l2.2-2.2a1 1 0 0 1 1-.25 11.4 11.4 0 0 0 3.6.57 1 1 0 0 1 1 1V20a1 1 0 0 1-1 1A17 17 0 0 1 3 4a1 1 0 0 1 1-1h3.5a1 1 0 0 1 1 1 11.4 11.4 0 0 0 .57 3.6 1 1 0 0 1-.25 1z"/></svg>
      <div>012 555 0148<br>012 555 0148</div>
    </div>

    <div class="contact contact-address">
      <svg width="12" height="12" viewBox="0 0 24 24"><path fill="#fff" d="M12 3 2 12h3v8h5v-5h4v5h5v-8h3z"/></svg>
      <div>Suite 2716, 58, Moreland St<br>Carrow Flats, NSW 2039</div>
    </div>

    <div class="contact contact-email">
      <svg width="16" height="12" viewBox="0 0 24 18"><rect x="1" y="1" width="22" height="16" fill="none" stroke="#fff" stroke-width="1.6"/><path d="M1 1l11 9 11-9" fill="none" stroke="#fff" stroke-width="1.6"/></svg>
      <div>derek@orvanepartners.com.au</div>
    </div>
  </section>

  <section class="card card-back" aria-label="Business card back">
    <svg class="card-shapes" viewBox="0 0 540 309" aria-hidden="true">
      <defs>
        <linearGradient id="redBack" x1="0" y1="0" x2="1" y2="1">
          <stop offset="0" stop-color="#e12a3d"/>
          <stop offset="1" stop-color="#a80d20"/>
        </linearGradient>
      </defs>
      <rect width="540" height="309" fill="url(#redBack)"/>
      <path d="M0,100 H190 Q214,100 224,120 L236,144 Q246,162 268,162 H400 Q424,162 434,182 L446,206 Q456,224 478,224 H540 V262 H0 Z" fill="var(--grey-edge)"/>
      <path d="M0,106 H186 Q208,106 218,124 L230,148 Q240,168 264,168 H396 Q418,168 428,186 L440,210 Q450,230 474,230 H540 V256 H0 Z" fill="var(--white)"/>
      <path d="M0,106 H120 V256 H0 Z" fill="var(--tab-grey)"/>
    </svg>
    <div class="person">
      <div class="person-name">DEREK FANSHAW</div>
      <div class="person-role">Managing Director</div>
    </div>
  </section>

</main>
</body>
</html>
```